Wedding invitation

Hello,

I would like the same attached image in a vertical rectangular 3D effect design, same colours,
but without text.

I would like eaxctly like the attachment design, in a long vertical, ration 16:9 size for social media.

```html
<!DOCTYPE html>
<html lang="en">
<head>
<meta charset="utf-8">
<title>Wedding Invitation Frame</title>
<link rel="stylesheet" href="https://fonts.googleapis.com/css2?family=Montserrat:wght@500&display=swap">
<style>
  :root {
    --page: #ffffff;
    --panel: #2b3447;
    --groove: #07090e;
    --molding: #2f384b;
    --gold-dark: #a8661b;
    --gold-light: #f7cd6c;
  }
  html, body {
    margin: 0;
    padding: 0;
    width: 907px;
    height: 1200px;
    overflow: hidden;
    background: var(--page);
    font-family: "Montserrat", sans-serif;
  }
  .invitation {
    display: block;
    width: 907px;
    height: 1200px;
  }
  .panel-surface { fill: var(--panel); }
  .panel-grain { filter: url(#leather-grain); }
  .line { fill: none; stroke-linejoin: miter; stroke-miterlimit: 3; }
  .molding-shadow { filter: drop-shadow(-4px 7px 7px rgba(0, 0, 0, 0.7)); }
  .molding-base { stroke: var(--groove); }
  .molding-bands { filter: url(#bevel-soft); }
  .molding-fill { fill: var(--molding); }
  .gold-shadow { filter: drop-shadow(-3px 5px 4px rgba(0, 0, 0, 0.75)); }
  .gold-rail { stroke: url(#gold-tone); }
  .gold-relief { filter: url(#bevel-gold); }
</style>
</head>
<body>
<svg class="invitation" viewBox="0 0 907 1200" xmlns="http://www.w3.org/2000/svg">
  <defs>
    <linearGradient id="gold-tone" x1="0" y1="0" x2="1" y2="1">
      <stop offset="0" stop-color="#f0b84e"/>
      <stop offset="0.3" stop-color="#d58b2a"/>
      <stop offset="0.55" stop-color="#f2bb50"/>
      <stop offset="0.8" stop-color="#cf8526"/>
      <stop offset="1" stop-color="#e8a840"/>
    </linearGradient>

    <filter id="leather-grain" x="0" y="0" width="100%" height="100%">
      <feTurbulence type="fractalNoise" baseFrequency="0.012 0.22" numOctaves="3" seed="4"/>
      <feColorMatrix type="matrix" values="0 0 0 0 0  0 0 0 0 0  0 0 0 0 0  0 0 0 -1.4 0.75"/>
      <feComposite in2="SourceGraphic" operator="in"/>
    </filter>

    <filter id="bevel-soft" x="-5%" y="-5%" width="110%" height="110%">
      <feGaussianBlur in="SourceAlpha" stdDeviation="1.6" result="blur"/>
      <feDiffuseLighting in="blur" surfaceScale="3" diffuseConstant="1.25" lighting-color="#ffffff" result="diffuse">
        <feDistantLight azimuth="235" elevation="50"/>
      </feDiffuseLighting>
      <feSpecularLighting in="blur" surfaceScale="3" specularConstant="0.35" specularExponent="18" lighting-color="#9aa6bd" result="spec">
        <feDistantLight azimuth="235" elevation="50"/>
      </feSpecularLighting>
      <feComposite in="spec" in2="SourceAlpha" operator="in" result="specIn"/>
      <feComposite in="SourceGraphic" in2="diffuse" operator="arithmetic" k1="1.15" k2="0" k3="0" k4="0" result="shaded"/>
      <feComposite in="shaded" in2="specIn" operator="arithmetic" k1="0" k2="1" k3="1" k4="0" result="lit"/>
      <feComposite in="lit" in2="SourceAlpha" operator="in"/>
    </filter>

    <filter id="bevel-gold" x="-5%" y="-5%" width="110%" height="110%">
      <feTurbulence type="fractalNoise" baseFrequency="0.05 0.3" numOctaves="2" seed="9" result="noise"/>
      <feColorMatrix in="noise" type="matrix" values="0 0 0 0 0.55  0 0 0 0 0.3  0 0 0 0 0.05  0 0 0 -1.2 0.55" result="patina"/>
      <feComposite in="patina" in2="SourceGraphic" operator="atop" result="textured"/>
      <feGaussianBlur in="SourceAlpha" stdDeviation="2.2" result="blur"/>
      <feDiffuseLighting in="blur" surfaceScale="5" diffuseConstant="1.3" lighting-color="#ffffff" result="diffuse">
        <feDistantLight azimuth="230" elevation="45"/>
      </feDiffuseLighting>
      <feSpecularLighting in="blur" surfaceScale="5" specularConstant="0.9" specularExponent="20" lighting-color="#ffe2a0" result="spec">
        <feDistantLight azimuth="230" elevation="45"/>
      </feSpecularLighting>
      <feComposite in="spec" in2="SourceAlpha" operator="in" result="specIn"/>
      <feComposite in="textured" in2="diffuse" operator="arithmetic" k1="1.1" k2="0" k3="0" k4="0" result="shaded"/>
      <feComposite in="shaded" in2="specIn" operator="arithmetic" k1="0" k2="1" k3="0.8" k4="0" result="lit"/>
      <feComposite in="lit" in2="SourceAlpha" operator="in"/>
    </filter>

    <path id="molding-line" d="
      M170 73 H470 Q500 73 514 110 H537 V135 H567
      V1003 H537 V1028 H514 Q500 1065 470 1065
      H170 Q140 1065 126 1028 H103 V1003 H73
      V135 H103 V110 H126 Q140 73 170 73 Z"/>

    <path id="gold-line" d="
      M190 105 H450 Q466 105 473 140 L501 163 H530
      V975 H501 L473 998 Q466 1033 450 1033
      H190 Q174 1033 167 998 L139 975 H110
      V163 H139 L167 140 Q174 105 190 105 Z"/>

    <mask id="molding-bands-mask" maskUnits="userSpaceOnUse" x="0" y="0" width="640" height="1138">
      <use href="#molding-line" class="line" stroke="#fff" stroke-width="40"/>
      <use href="#molding-line" class="line" stroke="#000" stroke-width="27"/>
      <use href="#molding-line" class="line" stroke="#fff" stroke-width="13"/>
    </mask>
  </defs>

  <g class="card" transform="translate(133.5 31)">
    <rect class="panel-surface" x="0" y="0" width="640" height="1138"/>
    <rect class="panel-grain" x="0" y="0" width="640" height="1138" fill="#000" opacity="0.16"/>

    <g class="molding">
      <g class="molding-shadow">
        <use href="#molding-line" class="line molding-base" stroke-width="40"/>
      </g>
      <g class="molding-bands">
        <rect class="molding-fill" x="0" y="0" width="640" height="1138" mask="url(#molding-bands-mask)"/>
      </g>
    </g>

    <g class="gold-frame">
      <g class="gold-shadow">
        <g class="gold-relief">
          <use href="#gold-line" class="line gold-rail" stroke-width="17"/>
        </g>
      </g>
    </g>
  </g>
</svg>
</body>
</html>
```